Simple Recipe eBook

I need the graphic work done for a simple recipe ebook, I have attached all of the required information for it, as well as our company logo. Further company info can be found at velqorith.com

I would like each recipe page to include 2 recipes, each recipe needs to include ingredients, picture, method, and nutritional info.

I would like the style to appear fresh and healthy, with lots of graphics and colours to match.
Please let me know if you need any guidance

Target Market(s)

Females aged from 15-25

Industry/Entity Type

It Company

```html
<!DOCTYPE html>
<html lang="en">
<head>
<meta charset="utf-8">
<title>Velqorith Recipe eBook</title>
<link href="https://fonts.googleapis.com/css2?family=Questrial&display=swap" rel="stylesheet">
<style>
:root{
  --teal:#3ec4c9;
  --ink:#2b2b2b;
  --muted:#8a8a8a;
  --rule:#bdbdbd;
  --frame:#1f1f1f;
  --mark:#4a4a4a;
  --paper:#ffffff;
}
*{box-sizing:border-box;margin:0;padding:0}
html,body{width:1200px;height:1000px;overflow:hidden;background:var(--paper)}
body{position:relative;font-family:"Questrial",sans-serif;color:var(--ink)}
.page{position:absolute;width:326px;height:460px;border:1px solid var(--frame);background:var(--paper);overflow:hidden}
.page > *{position:absolute}
.photo{border-radius:1px}
.recipe-title{color:var(--teal);font-size:6.4px;line-height:8px;font-weight:700;width:145px}
.ingredients{font-size:5.4px;line-height:6.6px;font-style:italic;width:145px}
.method{font-size:5.4px;line-height:6.6px;width:140px}
.method p{margin-bottom:6px}
.nutrition{width:120px}
.nutrition h4{font-size:6.4px;font-weight:400;margin-bottom:5px}
.nutrition dl{display:grid;grid-template-columns:1fr 1fr;column-gap:8px;row-gap:2px}
.nutrition dl div{font-size:3.6px;line-height:4.4px;color:var(--ink)}
.nutrition dd{color:var(--muted)}
.nutrition small{display:block;font-size:3.4px;margin-top:5px;color:var(--muted)}
.divider{left:16px;right:16px;border-top:1px dashed var(--rule)}
.section-head{color:var(--teal);font-size:13px;letter-spacing:.5px}
.salsa-head{font-style:normal;font-weight:700}
.snacks-badge{left:117px;top:86px;width:88px;height:88px;border-radius:50%;background:var(--teal);color:#fff;display:flex;align-items:center;justify-content:center;font-size:15px;letter-spacing:1px}
.snack-list{left:40px;width:245px;top:222px;list-style:none;text-align:center;font-size:6.2px;line-height:8px}
.snack-list li{margin-bottom:7px}
.brand-mark{left:131px;top:99px;width:66px;height:66px;border-radius:50%;background:var(--mark)}
.brand-name{left:0;width:100%;top:171px;text-align:center;font-size:27px;letter-spacing:2px;color:var(--mark)}
.brand-tagline{left:0;width:100%;top:206px;text-align:center;font-size:12px;color:var(--mark)}
.sign-off{left:0;width:100%;top:297px;text-align:center;font-size:14px;color:var(--teal)}
.contact{left:0;width:100%;top:365px;text-align:center;font-size:6.6px;line-height:8.4px;list-style:none}
.footer-note{font-size:5.6px}
</style>
</head>
<body>

<!-- Lunch page -->
<section class="page" style="left:107px;top:38px">
  <div class="photo" role="img" aria-label="Chicken noodle salad in a patterned bowl" style="left:16px;top:19px;width:145px;height:68px;background:linear-gradient(135deg,#3fb5b0,#d8cdb0 50%,#c9a575)"></div>
  <div class="method" style="left:172px;top:36px">
    <p>Cook the noodles according to the packet instructions, then drain and refresh.</p>
    <p>Place the noodles, chicken, spring onion, cucumber, carrot, chilli, herbs and kaffir lime leaves in a bowl. Toss to combine. Place the lime juice, sugar, fish sauce and soy sauce in a separate bowl, and stir to combine.</p>
    <p>To serve, pour dressing over the salad and toss to combine.</p>
  </div>
  <h3 class="recipe-title" style="left:18px;top:128px">Chicken Noodle Salad</h3>
  <div class="ingredients" style="left:18px;top:141px">500g dried egg noodles<br>2 cups shredded cooked chicken, cooled<br>2 spring onions, shredded<br>1/2 Lebanese cucumber, cut into matchsticks<br>1 carrot, cut into matchsticks<br>1 long red chilli, seeds removed, finely chopped<br>1 cup each mint and coriander leaves<br>2 kaffir lime leaves (see note), finely shredded<br>Juice of 1 lime<br>1 tablespoon each brown sugar, fish sauce and soy sauce</div>
  <div class="nutrition" style="left:172px;top:135px">
    <h4>Nutrition</h4>
    <dl>
      <div><dt>Energy</dt><dd>1620kJ</dd></div><div><dt>Dietary Fibre</dt><dd>4.0g</dd></div>
      <div><dt>Fat saturated</dt><dd>2.0g</dd></div><div><dt>Protein</dt><dd>32.0g</dd></div>
      <div><dt>Fat Total</dt><dd>7.0g</dd></div><div><dt>Cholesterol</dt><dd>80mg</dd></div>
      <div><dt>Carbohydrate sugars</dt><dd>6.0g</dd></div><div><dt>Sodium</dt><dd>950mg</dd></div>
      <div><dt>Carbohydrate Total</dt><dd>48.0g</dd></div>
    </dl>
    <small>All nutrition values are per serve.</small>
  </div>
  <hr class="divider" style="top:246px">
  <div class="photo" role="img" aria-label="Beetroot, carrot and hummus sandwich on a board" style="left:16px;top:254px;width:145px;height:95px;background:linear-gradient(135deg,#efe9e2,#b59a86 55%,#8b3a4a)"></div>
  <div class="method" style="left:172px;top:258px"><p>Spread 1 slice multigrain bread with 1 tablespoon bought hummus. Top with 1/2 stick celery, chopped, 20g (1/4 cup) grated carrot, and 3 slices canned beetroot. Top with another slice of bread. Cut in half.</p></div>
  <h3 class="recipe-title" style="left:18px;top:362px">Beetroot, carrot &amp; hummus sandwich</h3>
  <div class="ingredients" style="left:18px;top:381px">2 slices multigrain bread<br>1 tablespoon bought hummus<br>1/2 stick celery, chopped<br>20g (1/4 cup) grated carrot<br>3 slices canned beetroot</div>
  <div class="nutrition" style="left:172px;top:339px">
    <h4>Nutrition</h4>
    <dl>
      <div><dt>Energy</dt><dd>1110kJ</dd></div><div><dt>Dietary Fibre</dt><dd>8.0g</dd></div>
      <div><dt>Fat saturated</dt><dd>1.0g</dd></div><div><dt>Protein</dt><dd>11.0g</dd></div>
      <div><dt>Fat Total</dt><dd>6.0g</dd></div><div><dt>Cholesterol</dt><dd>0mg</dd></div>
      <div><dt>Carbohydrate sugars</dt><dd>9.0g</dd></div><div><dt>Sodium</dt><dd>560mg</dd></div>
      <div><dt>Carbohydrate Total</dt><dd>40.0g</dd></div>
    </dl>
    <small>All nutrition values are per serve.</small>
  </div>
</section>

<!-- Dinner page -->
<section class="page" style="left:437px;top:38px">
  <h2 class="section-head" style="left:24px;top:12px">DINNER</h2>
  <div class="photo" role="img" aria-label="Spicy tofu stir-fry in a blue bowl with chopsticks" style="left:24px;top:32px;width:140px;height:98px;background:linear-gradient(135deg,#2f5fa8,#c9803b 50%,#3d6fb3)"></div>
  <h3 class="recipe-title" style="left:180px;top:20px">Spicy Tofu Stir-Fry</h3>
  <div class="ingredients" style="left:180px;top:36px;width:132px">1 tablespoon vegetable oil<br>2 garlic cloves, crushed<br>150g small fresh shiitake mushrooms (or large shiitakes, roughly chopped)<br>200g pack spicy tofu, sliced<br>6 spring onions, cut into 3cm lengths<br>1 red capsicum, seeds removed, cut into thin strips<br>150g snow peas, trimmed<br>2 tablespoons soy sauce<br>2 tablespoons ketjap manis*<br>Cooked GoldGrain Brown Medium Grain Rice, to serve<br>Coriander leaves, to garnish</div>
  <div class="nutrition" style="left:24px;top:136px">
    <h4>Nutrition</h4>
    <dl>
      <div><dt>Energy</dt><dd>1290kJ</dd></div><div><dt>Dietary Fibre</dt><dd>6.0g</dd></div>
      <div><dt>Fat saturated</dt><dd>2.0g</dd></div><div><dt>Protein</dt><dd>18.0g</dd></div>
      <div><dt>Fat Total</dt><dd>12.0g</dd></div><div><dt>Cholesterol</dt><dd>0mg</dd></div>
      <div><dt>Carbohydrate sugars</dt><dd>8.0g</dd></div><div><dt>Sodium</dt><dd>1120mg</dd></div>
      <div><dt>Carbohydrate Total</dt><dd>34.0g</dd></div>
    </dl>
    <small>All nutrition values are per serve.</small>
  </div>
  <div class="method" style="left:180px;top:158px;width:132px">
    <p>Heat oil in a wok over high heat, add garlic and stir-fry for 30 seconds. Add mushrooms and tofu and stir-fry for 1 minute.</p>
    <p>Add spring onions, capsicum and snow peas, stir-fry for a further 1-2 minutes, then stir in soy and ketjap manis.</p>
    <p>Serve with rice and garnish with coriander.</p>
  </div>
  <hr class="divider" style="top:230px">
  <div class="photo" role="img" aria-label="Five spice beef with rice in white bowls" style="left:20px;top:245px;width:140px;height:95px;background:linear-gradient(135deg,#e8ecee,#6f8a5a 50%,#8a4a3a)"></div>
  <h3 class="recipe-title" style="left:172px;top:236px">Chinese five spice beef with rice</h3>
  <div class="ingredients" style="left:172px;top:248px;width:140px">1 1/2 tablespoons salt-reduced soy sauce<br>2 teaspoons Chinese five spice powder<br>500g beef rump steak, trimmed<br>2 teaspoons peanut oil<br>6 green onions, cut into 5cm lengths<br>2 bunches choy sum, leaves and stems separated, roughly chopped<br>2 tablespoons oyster sauce<br>Steamed GoldGrain Jasmine Fragrant Rice, to serve</div>
  <div class="method" style="left:172px;top:312px;width:140px">
    <p>Combine soy sauce and five spice in a shallow bowl. Add steak. Turn to coat. Heat half the oil in a frying pan over high heat. Cook steak for 2 to 3 minutes each side for medium or until cooked to your liking. Transfer to a plate. Rest, loosely covered with foil, for 5 minutes.</p>
    <p>Meanwhile, heat a wok over medium-high heat. Add remaining oil. Swirl to coat. Add onion and choy sum stems. Stir-fry for 2 minutes or until onion has softened. Add choy sum leaves, oyster sauce and 2 tablespoons cold water. Stir-fry for 2 to 3 minutes or until leaves have wilted.</p>
    <p>Slice steak. Serve with onion mixture and rice.</p>
  </div>
  <div class="nutrition" style="left:20px;top:357px">
    <h4>Nutrition</h4>
    <dl>
      <div><dt>Energy</dt><dd>1980kJ</dd></div><div><dt>Dietary Fibre</dt><dd>3.0g</dd></div>
      <div><dt>Fat saturated</dt><dd>3.0g</dd></div><div><dt>Protein</dt><dd>36.0g</dd></div>
      <div><dt>Fat Total</dt><dd>9.0g</dd></div><div><dt>Cholesterol</dt><dd>85mg</dd></div>
      <div><dt>Carbohydrate sugars</dt><dd>4.0g</dd></div><div><dt>Sodium</dt><dd>990mg</dd></div>
      <div><dt>Carbohydrate Total</dt><dd>52.0g</dd></div>
    </dl>
    <small>All nutrition values are per serve.</small>
  </div>
</section>

<!-- Dinner page 2 -->
<section class="page" style="left:768px;top:38px">
  <div class="photo" role="img" aria-label="Fried halloumi with chorizo and tomato salsa on a white plate" style="left:20px;top:11px;width:142px;height:96px;background:linear-gradient(135deg,#f2f2f2,#c0392b 50%,#d9a25a)"></div>
  <div class="ingredients" style="left:178px;top:12px;width:136px">1/3 cup (80ml) extra virgin olive oil<br>2 chorizo sausages, finely chopped<br>2 garlic cloves, thinly sliced<br>2 x 250g punnets cherry tomatoes, halved<br>Pinch chilli flakes<br>1 teaspoon caster sugar<br>1/4 cup (60ml) red wine vinegar<br>2 tablespoons finely chopped flat-leaf parsley, plus extra to serve<br>250g haloumi, cut into 8 slices<br>Chargrilled sourdough bread, to serve</div>
  <h3 class="recipe-title" style="left:20px;top:110px">Fried haloumi with chorizo &amp; cherry tomato salsa</h3>
  <div class="nutrition" style="left:20px;top:129px">
    <h4>Nutrition</h4>
    <dl>
      <div><dt>Energy</dt><dd>2450kJ</dd></div><div><dt>Dietary Fibre</dt><dd>3.0g</dd></div>
      <div><dt>Fat saturated</dt><dd>17.0g</dd></div><div><dt>Protein</dt><dd>29.0g</dd></div>
      <div><dt>Fat Total</dt><dd>46.0g</dd></div><div><dt>Cholesterol</dt><dd>78mg</dd></div>
      <div><dt>Carbohydrate sugars</dt><dd>6.0g</dd></div><div><dt>Sodium</dt><dd>2040mg</dd></div>
      <div><dt>Carbohydrate Total</dt><dd>8.0g</dd></div>
    </dl>
    <small>All nutrition values are per serve.</small>
  </div>
  <div class="method" style="left:178px;top:121px;width:136px">
    <p>Heat 2 tablespoons oil in a pan over medium-high heat. Cook chorizo, stirring, for 6-8 minutes until browned. Add garlic, tomato, chilli, sugar and 2 tablespoons vinegar. Cook, stirring occasionally, for 2-3 minutes until tomatoes have broken down and sauce thickens. Add parsley and remaining 1 tablespoon vinegar, then remove from heat.</p>
    <p>Meanwhile, heat remaining 2 tablespoons oil in a non-stick frypan over high heat and sear haloumi for 1 minute each side until golden brown and melting. Serve with chorizo salsa, extra parsley and sourdough.</p>
  </div>
  <hr class="divider" style="top:219px">
  <div class="photo" role="img" aria-label="Chicken fajita wraps with salad on a plate" style="left:16px;top:226px;width:145px;height:95px;background:linear-gradient(135deg,#f4f1ea,#d8c39a 45%,#4f8a3a)"></div>
  <div class="nutrition" style="left:166px;top:226px">
    <h4>Nutrition</h4>
    <dl>
      <div><dt>Energy</dt><dd>2710kJ</dd></div><div><dt>Dietary Fibre</dt><dd>7.0g</dd></div>
      <div><dt>Fat saturated</dt><dd>12.0g</dd></div><div><dt>Protein</dt><dd>58.0g</dd></div>
      <div><dt>Fat Total</dt><dd>34.0g</dd></div><div><dt>Cholesterol</dt><dd>190mg</dd></div>
      <div><dt>Carbohydrate sugars</dt><dd>6.0g</dd></div><div><dt>Sodium</dt><dd>690mg</dd></div>
      <div><dt>Carbohydrate Total</dt><dd>38.0g</dd></div>
    </dl>
    <small>All nutrition values are per serve.</small>
  </div>
  <h3 class="recipe-title" style="left:16px;top:337px;width:60px">Chicken fajitas</h3>
  <div class="ingredients" style="left:16px;top:357px;width:70px">2 teaspoons smoked paprika<br>1/4 cup (60ml) olive oil<br>1kg chicken thigh fillets, cut into 2cm thick slices<br>10 soft flour burritos<br>1/2 bunch watercress, trimmed<br>Creme fraiche or natural yoghurt, to serve</div>
  <div class="ingredients" style="left:88px;top:337px;width:74px"><span class="salsa-head">Salsa</span><br>3 medium ripe tomatoes, finely chopped<br>1 small Spanish onion, finely chopped<br>1 teaspoon finely grated lime rind<br>1 tablespoon lime juice<br>1 small red chilli (or to taste), finely chopped<br>1 avocado, peeled, coarsely chopped<br>1/3 cup chopped coriander<br>2 tablespoons olive oil</div>
  <div class="method" style="left:166px;top:316px;width:148px">
    <p>Preheat barbecue or chargrill pan on high. For salsa: combine tomatoes, onion, lime rind and juice, chilli, avocado, coriander and oil in a bowl. Taste and season with salt, pepper and sugar.</p>
    <p>Combine paprika and oil in a medium bowl. Add chicken and season with salt and pepper. Gently toss to combine. Cook chicken on barbecue or chargrill pan, turning occasionally for 8-10 minutes or until browned and cooked through. Place chicken on an oven tray, cover with foil and set aside in a warm place.</p>
    <p>Warm burritos on barbecue or chargrill pan until lightly charred.</p>
    <p>Place burritos on serving plates. Top with chicken and spoon over salsa. Add watercress and a dollop of creme fraiche. Fold to enclose filling and serve.</p>
  </div>
</section>

<!-- Dinner page 3 -->
<section class="page" style="left:107px;top:503px">
  <div class="photo" role="img" aria-label="Salmon cutlet with lime butter and green beans" style="left:18px;top:20px;width:145px;height:80px;background:linear-gradient(135deg,#f3f3f3,#e08a4a 50%,#5f8a3f)"></div>
  <div class="method" style="left:176px;top:20px;width:138px">
    <p>Place the butter in a small bowl. Add the coriander, lime rind, lime juice and cracked black pepper and mix until well combined. Refrigerate until ready to use.</p>
    <p>Heat a little olive oil in a non-stick frying pan over medium heat. Add 2 salmon cutlets and cook for 2-3 minutes each side or until cooked to your liking. Transfer to a plate and cover with foil to keep warm. Repeat with remaining salmon.</p>
    <p>To serve, divide the salmon cutlets among serving plates. Top with a little lime and coriander butter. Serve with steamed vegetables, if desired.</p>
  </div>
  <h3 class="recipe-title" style="left:18px;top:128px">Salmon cutlets with lime and coriander butter</h3>
  <div class="ingredients" style="left:18px;top:143px">100g butter, softened<br>2 tablespoons finely chopped coriander<br>2 teaspoons finely grated lime rind<br>2 teaspoons lime juice<br>cracked black pepper<br>4 salmon cutlets<br>steamed vegetables, to serve</div>
  <div class="nutrition" style="left:176px;top:132px">
    <h4>Nutrition</h4>
    <dl>
      <div><dt>Energy</dt><dd>2150kJ</dd></div><div><dt>Dietary Fibre</dt><dd>0g</dd></div>
      <div><dt>Fat saturated</dt><dd>17.0g</dd></div><div><dt>Protein</dt><dd>34.0g</dd></div>
      <div><dt>Fat Total</dt><dd>41.0g</dd></div><div><dt>Cholesterol</dt><dd>160mg</dd></div>
      <div><dt>Carbohydrate sugars</dt><dd>0g</dd></div><div><dt>Sodium</dt><dd>210mg</dd></div>
      <div><dt>Carbohydrate Total</dt><dd>0g</dd></div>
    </dl>
    <small>All nutrition values are per serve.</small>
  </div>
  <hr class="divider" style="top:222px">
  <div class="photo" role="img" aria-label="Tuna and olive fettuccine in a bowl" style="left:18px;top:232px;width:145px;height:95px;background:linear-gradient(135deg,#3fa86a,#f0e6d2 45%,#e0b070)"></div>
  <h3 class="recipe-title" style="left:176px;top:232px">Super-fast tuna and olive fettuccine</h3>
  <div class="ingredients" style="left:176px;top:245px;width:138px">375g dried fettuccine pasta<br>425g can tuna in oil<br>1 medium red onion, finely chopped<br>1 garlic clove, crushed<br>2 tablespoons roughly chopped drained capers<br>400g can Italian tomatoes with sliced olives<br>1 cup torn basil leaves<br>Shaved parmesan, to serve</div>
  <div class="nutrition" style="left:18px;top:336px">
    <h4>Nutrition</h4>
    <dl>
      <div><dt>Energy</dt><dd>2870kJ</dd></div><div><dt>Dietary Fibre</dt><dd>5.0g</dd></div>
      <div><dt>Fat saturated</dt><dd>5.0g</dd></div><div><dt>Protein</dt><dd>38.0g</dd></div>
      <div><dt>Fat Total</dt><dd>26.0g</dd></div><div><dt>Cholesterol</dt><dd>40mg</dd></div>
      <div><dt>Carbohydrate sugars</dt><dd>6.0g</dd></div><div><dt>Sodium</dt><dd>620mg</dd></div>
      <div><dt>Carbohydrate Total</dt><dd>70.0g</dd></div>
    </dl>
    <small>All nutrition values are per serve.</small>
  </div>
  <div class="method" style="left:176px;top:318px;width:138px">
    <p>Cook pasta in a saucepan of boiling, salted water following packet directions until tender. Drain. Return to pan.</p>
    <p>Meanwhile, drain tuna, reserving 2 tablespoons oil. Heat oil in a non-stick frying pan over medium heat. Add onion and garlic. Cook for 3 to 4 minutes or until onion has softened.</p>
    <p>Stir in capers, tomato and 1/2 cup cold water. Bring to a simmer. Simmer for 10 to 12 minutes or until sauce has thickened.</p>
    <p>Using a fork, flake tuna. Add tuna, tomato mixture and basil to pasta. Toss gently over low heat for 1 to 2 minutes or until heated through. Divide between bowls. Serve with parmesan.</p>
  </div>
  <p class="footer-note" style="left:16px;top:440px">Find more great recipes at platefeed.com.au</p>
</section>

<!-- Snacks page -->
<section class="page" style="left:437px;top:503px">
  <div class="snacks-badge">SNACKS</div>
  <ul class="snack-list">
    <li>-A small amount of dried fruit</li>
    <li>-A handfull of mixed nuts</li>
    <li>-Fruits</li>
    <li>-Carrot and celery sticks with hummus</li>
    <li>-A scoop of whey protein mixed with water or soy milk</li>
    <li>-Plain yogurt with a bit of honey</li>
  </ul>
</section>

<!-- Back cover -->
<section class="page" style="left:768px;top:503px">
  <div class="brand-mark" aria-hidden="true"></div>
  <p class="brand-name">VELQORITH</p>
  <p class="brand-tagline">eat. grow. glow.</p>
  <p class="sign-off">Good Luck!</p>
  <ul class="contact">
    <li>velqorith.com</li>
    <li>fb.com/velqorith</li>
    <li>instagram.com/velqorith</li>
  </ul>
</section>

</body>
</html>
```